Footwear & Apparel Business to Business Presentation (B2B)

We are looking for a Business to Business presentation that is simple, clean, and easy to understand.

We would like the steps to be laid out with simple graphics indicating steps 1, 2 , 3 with circles / arrows. Colours are acceptable. This is a tool to engage potential customers so needs to be very clear and easy to understand.

our logo is attached.
Updates

Target Market(s)

women aged 30 plus

Industry/Entity Type

Business

Font styles to use
Serif
Sans Serif

Requirements
Must have
• 2 pages:
• 1st page should be our logo and who we are:
• Coral Ridge Of Textiles
• contact: info@crot.com.au
• We are a wholesale and distribution company of footwear and apparel
• We specialize in clearing aged stock through flash sales channels in Australia and New Zealand.
• We offer suppliers an alternative inventory distribution channel.
• Take advantage of the reverse seasonality - when you can't move your winter stock, We Can!
• presentation black and white
• must look clean , simple , contemporary
• 2nd Page:
• clear detailed step by step process
• graphics demonstrating this
• suggestions:
• step by step on an pebble flatscreen with an arrow between each step with an image on each screen and notes on the side
• we need the following 3 steps on our brief:
• 1 - we buy upfront and handle all processes
• 2 - $ in your bank
• 3 - goods shipped to Australia / New Zealand
Nice to have
• suggestions:
• -use graphics to show moving stock from north america to australia & New zealand
• -maybe a global map
• -icons showing money and transportation
• -demonstrate the 3 steps in pebble windows
• - show the graphics / icons as a backdrop and text on top

```html
<!DOCTYPE html>
<html lang="en">
<head>
<meta charset="utf-8">
<title>Coral Ridge Of Textiles – How It Works</title>
<link rel="stylesheet" href="https://fonts.googleapis.com/css2?family=Open+Sans:wght@400;700;800&display=swap">
<style>
  :root {
    --backdrop: #ececec;
    --paper: #ffffff;
    --ink: #333333;
    --label: #222222;
    --chin: #f2f2f2;
    --footer-text: #e6e6e6;
  }
  * { margin: 0; padding: 0; box-sizing: border-box; }
  html, body {
    width: 1200px; height: 1000px; overflow: hidden;
    background: var(--backdrop);
    font-family: "Open Sans", Arial, sans-serif;
    color: var(--ink);
  }
  .page {
    position: absolute; left: 148px; top: 50px;
    width: 637px; height: 900px;
    background: var(--paper);
  }
  .page-art { position: absolute; left: 0; top: 0; }
  .step-number {
    position: absolute; font-weight: 800; font-size: 28px; line-height: 1;
  }
  .step-note {
    position: absolute; font-weight: 700; font-size: 15px; line-height: 17px;
  }
  .step-note .small { font-size: 13.5px; }
  .big-dollar {
    position: absolute; font-weight: 800; font-size: 52px; line-height: 1;
  }
  .footer-band {
    position: absolute; left: 0; bottom: 0; width: 637px; height: 62px;
    background: var(--ink);
    display: flex; align-items: center; justify-content: center; gap: 10px;
  }
  .brand-mark {
    width: 16px; height: 16px; border-radius: 50%;
    border: 1px solid var(--footer-text);
  }
  .brand-name {
    color: var(--footer-text); font-size: 7px; font-weight: 400;
    letter-spacing: 4px; text-transform: uppercase;
  }
  .page-label {
    position: absolute; left: 901px; top: 422px;
    width: 299px; height: 91px;
    background: var(--label); color: var(--paper);
    font-family: Arial, Helvetica, sans-serif;
    font-size: 44px; font-weight: 400;
    display: flex; align-items: center; padding-left: 40px;
  }
  .page-label strong { font-weight: 700; margin-left: 12px; }
</style>
</head>
<body>
<div class="page">
  <svg class="page-art" width="637" height="900" viewBox="0 0 637 900" xmlns="http://www.w3.org/2000/svg">
    <defs>
      <linearGradient id="chinShade" x1="0" y1="0" x2="0" y2="1">
        <stop offset="0" stop-color="#ffffff"/>
        <stop offset="1" stop-color="#e2e2e2"/>
      </linearGradient>
      <linearGradient id="mapTone" x1="0" y1="0" x2="1" y2="1">
        <stop offset="0" stop-color="#bdbdbd"/>
        <stop offset="1" stop-color="#e4e4e4"/>
      </linearGradient>
      <g id="monitor">
        <rect x="1.5" y="1.5" width="212" height="170" rx="8" fill="var(--paper)" stroke="var(--ink)" stroke-width="3"/>
        <rect x="8" y="8" width="199" height="130" fill="var(--ink)"/>
        <rect x="14" y="14" width="187" height="118" fill="var(--paper)"/>
        <path d="M9 168 Q108 150 206 150 L206 164 Q206 168 202 168 Z" fill="url(#chinShade)"/>
        <path d="M70 173 L74 196 Q74 198 66 198 Q64 198 64 201 Q64 203 67 203 L148 203 Q151 203 151 201 Q151 198 149 198 Q141 198 141 196 L145 173" fill="var(--paper)" stroke="var(--ink)" stroke-width="3" stroke-linejoin="round"/>
      </g>
      <g id="cycleSegment">
        <path d="M143.5 79.3 A36 36 0 0 1 126 104.2" fill="none" stroke="var(--ink)" stroke-width="18"/>
        <polygon points="120,93.8 133,116.3 114.3,108.5" fill="var(--ink)" stroke="var(--paper)" stroke-width="1.5" stroke-linejoin="round"/>
      </g>
    </defs>

    <!-- Step 1: cycle of money -->
    <g transform="translate(100 60)">
      <use href="#monitor"/>
      <g class="cycle-icon">
        <use href="#cycleSegment"/>
        <use href="#cycleSegment" transform="rotate(90 108 73)"/>
        <use href="#cycleSegment" transform="rotate(180 108 73)"/>
        <use href="#cycleSegment" transform="rotate(270 108 73)"/>
        <circle cx="108" cy="73" r="21" fill="var(--ink)" stroke="var(--paper)" stroke-width="3"/>
        <text x="108" y="84" font-family="Open Sans, sans-serif" font-weight="800" font-size="30" text-anchor="middle" fill="var(--paper)">$</text>
      </g>
    </g>

    <!-- Step 2: bank -->
    <g transform="translate(100 324)">
      <use href="#monitor"/>
      <g class="bank-icon" fill="var(--ink)">
        <polygon points="38,50 84,23 130,50"/>
        <text x="84" y="46" font-family="Open Sans, sans-serif" font-weight="800" font-size="17" text-anchor="middle" fill="var(--paper)">$</text>
        <rect x="38" y="52" width="92" height="6"/>
        <rect x="45" y="61" width="15" height="40"/>
        <rect x="76" y="61" width="15" height="40"/>
        <rect x="107" y="61" width="15" height="40"/>
        <rect x="40" y="104" width="88" height="4"/>
        <rect x="36" y="110" width="96" height="4"/>
        <rect x="32" y="116" width="104" height="4"/>
      </g>
      <text x="160" y="110" font-family="Open Sans, sans-serif" font-weight="800" font-size="80" text-anchor="middle" fill="var(--ink)">$</text>
    </g>

    <!-- Step 3: shipping route -->
    <g transform="translate(100 587)">
      <use href="#monitor"/>
      <g role="img" aria-label="World map showing North America, Australia and New Zealand">
        <rect x="16" y="16" width="183" height="114" fill="url(#mapTone)"/>
      </g>
      <g class="route-arrows" fill="none" stroke="var(--ink)" stroke-width="2">
        <path d="M72 35 Q125 18 143 58"/>
        <path d="M72 35 Q170 10 187 86"/>
      </g>
      <polygon points="136,54 150,54 145,68" fill="var(--ink)"/>
      <polygon points="180,82 194,80 190,96" fill="var(--ink)"/>
    </g>

    <!-- Connecting arrows -->
    <g stroke="var(--ink)" stroke-width="3">
      <line x1="432" y1="195" x2="432" y2="310"/>
      <line x1="432" y1="458" x2="432" y2="572"/>
    </g>
    <polygon points="418,305 446,305 432,333" fill="var(--ink)"/>
    <polygon points="418,568 446,568 432,596" fill="var(--ink)"/>
  </svg>

  <span class="step-number" style="left:336px; top:121px;">1</span>
  <p class="step-note" style="left:369px; top:104px;">We buy upfront<br>and<br>handle all processes</p>

  <span class="step-number" style="left:333px; top:387px;">2</span>
  <span class="big-dollar" style="left:366px; top:369px;">$</span>
  <p class="step-note" style="left:400px; top:378px;">in<br>your bank</p>

  <span class="step-number" style="left:334px; top:652px;">3</span>
  <p class="step-note" style="left:369px; top:642px;">Goods shipped to<br><span class="small">Australia / New Zealand</span></p>

  <footer class="footer-band">
    <span class="brand-name">Coral Ridge Of Textiles</span>
    <span class="brand-mark"></span>
  </footer>
</div>

<div class="page-label">Page<strong>2</strong></div>
</body>
</html>
```